Electrical construction company
Industrial Construction, mining construction, Electrical works
Creative Brief
Construction
brightlinepowerworks.com.au
Electrical construction. Experienced in the construction industry,20 year. High quality work First class customer services Able to be flexible and suit customer requirements Provide QA documention and qualified testers. Hazardous Area trained personel 5 star safety rating
Modern
Blue same as in logo
PixelRidge PixelRidge
PH, Kindly check your private messages. Thanks!
owenharlow owenharlow
#59 can you use the picture i suppied as the back drop, the one of the plant. Thankyou
Phone numnber is 1800 VOLTEK Address is 17/9 Marlin Court, Belmont, western australia Thankyou
#50 can you use the picture provided of the plant Thankyou
Will need to include Lic. No. EC38157 somewhere also
Not so interested about have a testimonial on he front page Maybe use the other pictures as the main thankyou
i have payed 700 would have thought the prise was 700?
Would like the page to fit on the page without scrolling down
Like the idea of the map with address
HubKeeper HubKeeper

```html
<!DOCTYPE html>
<html lang="en">
<head>
<meta charset="utf-8">
<title>Brightline Powerworks</title>
<link href="https://fonts.googleapis.com/css2?family=Open+Sans:wght@400;600;700&display=swap" rel="stylesheet">
<style>
:root{
  --blue:#1a8fd6;
  --blue-dark:#0b6db3;
  --blue-light:#4fb3ea;
  --red:#d9261c;
  --green:#5a9e1c;
  --green-light:#8cc63f;
  --grey:#5a5a5a;
  --text:#666;
  --line:#d8d8d8;
  --white:#fff;
}
*{box-sizing:border-box;margin:0;padding:0}
html,body{width:1200px;height:1086px;overflow:hidden}
body{font-family:"Open Sans",Arial,sans-serif;background:#f4f4f4;color:var(--text);position:relative}
.page{position:absolute;inset:0;background:linear-gradient(#fff 0,#f6f6f6 440px,#eee 840px)}
.wrap{position:absolute;left:150px;width:900px}

.header{top:0;height:100px}
.brand{position:absolute;left:0;top:26px;display:flex;align-items:center;gap:12px}
.brand-dot{width:50px;height:50px;border-radius:50%;background:var(--blue)}
.brand-name{font-size:32px;font-weight:700;color:var(--blue);letter-spacing:1px;line-height:1;white-space:nowrap}
.header-contact{position:absolute;right:0;top:8px;display:flex;align-items:center;gap:26px;white-space:nowrap}
.licence{font-size:19px;color:var(--red);font-weight:600}
.licence b{color:var(--grey);font-weight:600}
.phone{display:flex;align-items:center;gap:8px;font-size:19px;color:var(--grey)}
.phone svg{width:26px;height:26px;flex:none}

.nav{top:100px;height:40px;background:linear-gradient(var(--green-light),var(--green));display:flex;border-radius:4px 4px 0 0}
.nav a{flex:1;display:flex;align-items:center;justify-content:center;color:#fff;font-size:15px;text-decoration:none;text-transform:uppercase;border-right:1px solid rgba(255,255,255,.25);white-space:nowrap}
.nav a.active{background:var(--red);flex:.6;border-radius:4px 0 0 0}

.hero{position:absolute;left:0;top:140px;width:1200px;height:295px;background:linear-gradient(180deg,#c9d6e0 0%,#a7b3bb 35%,#6b5a45 62%,#3a2f26 100%)}
.hero-caption{position:absolute;left:170px;top:258px;color:#fff;font-size:22px;background:rgba(0,0,0,.25);padding:2px 8px}
.hero-arrow{position:absolute;top:125px;width:34px;height:34px;border-radius:50%;background:rgba(40,40,40,.7)}
.hero-arrow svg{width:34px;height:34px}
.hero-dots{position:absolute;left:1010px;top:275px;display:flex;gap:6px}
.hero-dots i{width:11px;height:11px;border-radius:50%;background:rgba(255,255,255,.6)}
.hero-dots i:first-child{background:#fff}

.welcome{top:447px}
.welcome h2{font-size:16px;color:var(--red);font-weight:700;text-transform:uppercase}
.welcome-photo{position:absolute;left:0;top:28px;width:125px;height:90px;background:linear-gradient(135deg,#8fa8bd,#d9a441 60%,#5a6a78)}
.welcome p{position:absolute;left:140px;top:26px;width:760px;font-size:12.5px;line-height:17.5px}
.more{font-size:14px;color:var(--green);font-weight:700;display:inline-flex;align-items:center;gap:4px}
.welcome .more{position:absolute;right:0;top:120px}
.more i{width:14px;height:14px;border-radius:50%;background:var(--green);display:inline-block}

.features{top:595px;display:flex;justify-content:space-between}
.feature{width:290px;height:240px;background:#fff;border:1px solid var(--line);box-shadow:0 2px 4px rgba(0,0,0,.12);padding:14px 14px;position:relative}
.feature h3{display:flex;align-items:center;gap:8px;font-size:12.5px;color:var(--red);text-transform:uppercase;font-weight:600;white-space:nowrap}
.feature h3 span.icon{width:38px;height:38px;border-radius:50%;background:var(--blue);flex:none}
.feature p{margin-top:16px;font-size:12.5px;line-height:17.5px}
.btn{position:absolute;right:14px;bottom:14px;background:linear-gradient(var(--green-light),var(--green));color:#fff;font-size:13px;padding:4px 10px;border-radius:3px;display:flex;align-items:center;gap:6px}
.btn i{width:12px;height:12px;border-radius:50%;background:#fff;display:inline-block}

.footer{position:absolute;left:0;top:850px;width:1200px;height:196px;background:linear-gradient(var(--blue-light),var(--blue-dark))}
.footer .wrap{top:12px;height:180px;display:flex;gap:30px}
.footer h4{color:#fff;font-size:17px;font-weight:400;margin-bottom:10px}
.col-news{width:230px}
.field{width:130px;height:24px;background:var(--blue-dark);border:1px solid rgba(255,255,255,.4);color:#fff;font-size:12px;padding:3px 8px;margin-bottom:10px}
.subscribe{display:inline-block;background:var(--green-light);color:#fff;font-size:13px;padding:3px 10px;border-radius:3px}
.col-links{width:200px}
.col-links ul{list-style:none}
.col-links li{color:#fff;font-size:12.5px;line-height:20px;border-bottom:1px solid rgba(255,255,255,.25);padding-left:12px;position:relative}
.col-links li::before{content:"";position:absolute;left:0;top:7px;border:4px solid transparent;border-left-color:#fff}
.col-feed{width:230px}
.tweet{display:flex;gap:8px;margin-bottom:8px}
.tweet i{width:32px;height:32px;background:#9ab8cc;flex:none}
.tweet p{color:#fff;font-size:11px;line-height:15px}
.follow{color:#fff;font-size:12px;display:flex;align-items:center;gap:6px}
.follow i{width:18px;height:18px;border-radius:50%;background:#fff}
.col-contact{width:160px}
.map{width:160px;height:95px;background:linear-gradient(135deg,#e8e2d2,#c9dbb4 50%,#e0d8c4)}
.addr{color:#fff;font-size:12px;line-height:16px;margin-top:6px}

.bottom{position:absolute;left:0;top:1046px;width:1200px;height:40px;background:linear-gradient(var(--green-light),var(--green))}
.bottom p{position:absolute;left:150px;top:11px;color:#fff;font-size:12px}
.social{position:absolute;right:150px;top:8px;display:flex;gap:8px}
.social i{width:24px;height:24px;border-radius:3px;background:#fff;opacity:.9}
</style>
</head>
<body>
<div class="page">
  <header class="wrap header">
    <div class="brand"><span class="brand-dot"></span><span class="brand-name">BRIGHTLINE POWERWORKS</span></div>
    <div class="header-contact">
      <div class="licence"><b>Lic. No.</b> EC38157</div>
      <div class="phone">
        <svg viewBox="0 0 30 30"><circle cx="15" cy="15" r="14" fill="none" stroke="#5a5a5a" stroke-width="2"/><path d="M10 8l3 0 1 4-2 1.5a9 9 0 0 0 4.5 4.5l1.5-2 4 1 0 3a2 2 0 0 1-2 2A13 13 0 0 1 8 10a2 2 0 0 1 2-2z" fill="#5a5a5a"/></svg>
        1800-865-358
      </div>
    </div>
  </header>

  <nav class="wrap nav">
    <a class="active">Home</a><a>About Us</a><a>Our Capabilities</a><a>Projects</a><a>News and Events</a><a>Contact Us</a>
  </nav>

  <section class="hero" role="img" aria-label="Industrial plant under construction with cranes and steel structures">
    <div class="hero-caption">Experienced in the construction industry, 20 year.</div>
    <div class="hero-arrow" style="left:152px"><svg viewBox="0 0 34 34"><path d="M20 10l-7 7 7 7" fill="none" stroke="#fff" stroke-width="3"/></svg></div>
    <div class="hero-arrow" style="left:1014px"><svg viewBox="0 0 34 34"><path d="M14 10l7 7-7 7" fill="none" stroke="#fff" stroke-width="3"/></svg></div>
    <div class="hero-dots"><i></i><i></i><i></i><i></i></div>
  </section>

  <section class="wrap welcome">
    <h2>Welcome to Brightline Powerworks</h2>
    <div class="welcome-photo" role="img" aria-label="Electrician in safety gear at work on site"></div>
    <p>Lorem ipsum dolor sit amet, consectetur adipisicing elit, sed do eiusmod tempor incididunt ut labore et dolore magna aliqua. Ut enim ad minim veniam, quis nostrud exercitation ullamco laboris nisi ut aliquip ex ea commodo consequat. Lorem ipsum dolor sit amet consectetur adipisicing elit, sed do eiusmod tempor incididunt ut labore et dolore magna aliqua. Ut enim ad minim veniam, quis nostrud exercitation ullamco laboris nisi ut aliquip ex ea commodo consequat. Lorem ipsum dolor sit amet, consectetur adipisicing elit, sed do eiusmod tempor incididunt ut labore et dolore magna aliqua. Ut enim ad minim veniam, quis nostrud exercitation ullamco laboris nisi ut aliquip ex ea commodo.</p>
    <span class="more">read more <i></i></span>
  </section>

  <section class="wrap features">
    <article class="feature">
      <h3><span class="icon"></span>Electrical Construction</h3>
      <p>Lorem ipsum dolor sit amet consectetur adipisicing elit, sed do eiusmod tempor incididunt ut labore et dolore magna aliqua. Ut enim ad minim veniam, quis nostrud exercitation ullamco laboris nisi ut aliquip ex ea commodo consequat.</p>
      <span class="btn">Read More <i></i></span>
    </article>
    <article class="feature">
      <h3><span class="icon"></span>High Quality Work</h3>
      <p>Lorem ipsum dolor sit amet consectetur adipisicing elit, sed do eiusmod tempor incididunt ut labore et dolore magna aliqua. Ut enim ad minim veniam, quis nostrud exercitation ullamco laboris nisi ut aliquip ex ea commodo consequat.</p>
      <span class="btn">Read More <i></i></span>
    </article>
    <article class="feature">
      <h3><span class="icon"></span>First Class Customer Services</h3>
      <p>Lorem ipsum dolor sit amet consectetur adipisicing elit, sed do eiusmod tempor incididunt ut labore et dolore magna aliqua. Ut enim ad minim veniam, quis nostrud exercitation ullamco laboris nisi ut aliquip ex ea commodo consequat.</p>
      <span class="btn">Read More <i></i></span>
    </article>
  </section>

  <footer class="footer">
    <div class="wrap">
      <div class="col-news">
        <h4>Newsletter Signup</h4>
        <div class="field">First Name *</div>
        <div class="field">Last Name *</div>
        <div class="field">Email *</div>
        <span class="subscribe">Subscribe</span>
      </div>
      <div class="col-links">
        <h4>Quick Link</h4>
        <ul><li>Home</li><li>About Us</li><li>Our Capabilities</li><li>Projects</li><li>News and Events</li><li>Contact Us</li></ul>
      </div>
      <div class="col-feed">
        <h4>Chirpline Feed</h4>
        <div class="tweet"><i></i><p>Lorem ipsum dolor, consectetur adipisicing elit. Quisque.</p></div>
        <div class="tweet"><i></i><p>Lorem ipsum dolor, consectetur adipisicing elit. Quisque.</p></div>
        <div class="tweet"><i></i><p>Lorem ipsum dolor, consectetur adipisicing elit. Quisque.</p></div>
        <div class="follow"><i></i>Follow us on Chirpline</div>
      </div>
      <div class="col-contact">
        <h4>Contact Us</h4>
        <div class="map" role="img" aria-label="Street map showing the office location"></div>
        <p class="addr">17/9 Marlin Court, Belmont, western australia</p>
      </div>
    </div>
  </footer>

  <div class="bottom">
    <p>© 2013 Electrical construction company | All Rights Reserved</p>
    <div class="social"><i></i><i></i><i></i></div>
  </div>
</div>
</body>
</html>
```